New Design for our Credit Cards tank.

Our company has petrol stations in Spain and the rest of Europe. We are specialized on the international transport companies. For This We Have our own "credit cards tank" With These cards you can refill in different countries (all over Europe) fast, save and cheap. We would like to redesign our credit cards tank. We are looking for something more modern, elegant and clean. We have three card types: - Spanish Card (Spain Card): This card is for customers who make refills at our service stations in Spain. This card is for Diesel product and used by transport companies. The printer prints the data That on This card can print in white. The fields we are print on the card, card number, holder, registration number and expiration date. - Europe Card (Europe Card): This card is for customers who refills at our service stations in Europe. The printer prints the data That on This card can not print in white. The fields we are print on the card, card number, holder, registration number and expiration date. - Red Card (Gasoleo Bonificado): This card is for a Customer WHO refills Red Diesel for a refrigerator units in our service stations in Spain. The printer prints the data That on This card can print in white. The fields we are print on the card, card number, holder, registration number and expiration date. Very important for us is That on the back side, you respect the text shown on the cards and the magnetic stripe zone. Of course Also the name of the company BRENVICOR must be seen there. Also would be great if our colors (its blue colors) will be respected. If You have any questions or Suggest we are pleased to get your comments or contacts. Thanks in advance Brenvicor

Target Market(s)

Our customers

Industry/Entity Type

Credit Card

Font styles to use
Sans Serif

Colors
3176b5
0255a3
85acd3
cedeed
85cae6
33a6d7
0692cd
f59195
f04a50

Requirements
Must have
• The only thing we Have to keep the fields on front and back text. The credit card 85mm x 54mm are meassures.

```html
<!DOCTYPE html>
<html lang="es">
<head>
<meta charset="utf-8">
<title>Brenvicor – Red Diesel Card</title>
<link rel="stylesheet" href="https://fonts.googleapis.com/css2?family=Open+Sans:wght@400;600;700;800&family=Orbitron:wght@700&display=swap">
<style>
  :root {
    --backdrop: #d6d6d6;
    --card-red: #d5161e;
    --card-red-dark: #a50a10;
    --card-red-light: #e42a30;
    --print-yellow: #f3ea12;
    --ink-shadow: #5a0a0a;
    --stripe: #111111;
    --text-white: #ffffff;
    --brand-blue: #0255a3;
    --photo-grey: #8e9296;
    --photo-blue: #3176b5;
    --photo-green: #a6b79a;
    --photo-light: #cfd4d2;
  }
  * { box-sizing: border-box; margin: 0; padding: 0; }
  html, body {
    width: 1200px; height: 915px; overflow: hidden;
    background: var(--backdrop);
    font-family: "Open Sans", Arial, sans-serif;
  }
  .sheet {
    position: relative; width: 1200px; height: 915px;
    display: flex; flex-direction: column; align-items: center; justify-content: center;
    gap: 48px;
  }
  .card {
    position: relative; width: 640px; height: 407px;
    border-radius: 26px; overflow: hidden;
    box-shadow: 0 6px 18px rgba(0,0,0,.25);
  }

  /* ---------- Front ---------- */
  .card-front { background: var(--card-red); }
  .card-front__photo {
    position: absolute; inset: 0;
    background:
      radial-gradient(ellipse 90px 130px at 130px 150px, var(--photo-blue) 0%, rgba(49,118,181,0) 100%),
      linear-gradient(100deg, #3e4144 0%, var(--photo-grey) 22%, var(--photo-green) 48%, var(--photo-light) 70%);
  }
  .card-front__panel { position: absolute; inset: 0; width: 100%; height: 100%; }
  .card-front__brand {
    position: absolute; left: 96px; top: 40px;
    display: flex; align-items: center; gap: 10px;
    font-weight: 700; font-size: 44px; color: var(--brand-blue); letter-spacing: -0.5px;
    white-space: nowrap;
  }
  .card-front__brand-dot {
    width: 20px; height: 20px; border-radius: 50%; background: var(--brand-blue);
  }
  .print {
    position: absolute; color: var(--print-yellow); white-space: nowrap;
    text-shadow: 1px 1px 0 var(--ink-shadow), 2px 2px 2px rgba(0,0,0,.45);
  }
  .card-front__type {
    right: 44px; top: 40px;
    font-weight: 800; font-style: italic; font-size: 19px; letter-spacing: 1px;
  }
  .card-front__number {
    left: 40px; top: 196px;
    font-family: "Orbitron", "Courier New", monospace; font-weight: 700;
    font-size: 33px; letter-spacing: 2px; word-spacing: 8px;
  }
  .card-front__holder {
    left: 262px; top: 256px;
    font-weight: 600; font-size: 30px; letter-spacing: 0.5px;
  }
  .card-front__expiry {
    left: 196px; top: 306px; font-weight: 700; font-size: 12px; text-shadow: none;
  }
  .card-front__cvv {
    left: 500px; top: 350px; font-weight: 700; font-size: 13px; text-shadow: none;
  }

  /* ---------- Back ---------- */
  .card-back {
    background: linear-gradient(135deg, var(--card-red-light) 0%, var(--card-red) 45%, var(--card-red-dark) 100%);
  }
  .card-back__stripe {
    position: absolute; left: 0; right: 0; top: 34px; height: 70px; background: var(--stripe);
  }
  .card-back__text {
    position: absolute; left: 44px; right: 44px; top: 128px;
    color: var(--text-white); font-size: 15px; line-height: 1.45;
  }
  .card-back__text p + p { margin-top: 18px; }
  .card-back__web {
    position: absolute; right: 44px; bottom: 34px;
    color: var(--print-yellow); font-weight: 600; font-size: 19px; white-space: nowrap;
  }
</style>
</head>
<body>
<main class="sheet">

  <section class="card card-front" aria-label="Anverso de la tarjeta">
    <div class="card-front__photo" role="img" aria-label="Fotografía de un surtidor de gasóleo con la manguera azul"></div>
    <svg class="card-front__panel" viewBox="0 0 640 407" preserveAspectRatio="none" aria-hidden="true">
      <defs>
        <linearGradient id="redPanel" x1="0" y1="0" x2="1" y2="1">
          <stop offset="0" stop-color="#e42a30"/>
          <stop offset="1" stop-color="#c40f17"/>
        </linearGradient>
      </defs>
      <polygon points="190,407 430,0 640,0 640,407" fill="url(#redPanel)"/>
    </svg>
    <div class="card-front__brand">
      <span class="card-front__brand-dot"></span>
      <span class="card-front__brand-name">Brenvicor</span>
    </div>
    <div class="print card-front__type">RED DIESEL CARD</div>
    <div class="print card-front__number">1234 4567 1234 4567</div>
    <div class="print card-front__holder">MARLO DEVANE</div>
    <div class="print card-front__expiry">VALID THRU: 11/2019</div>
    <div class="print card-front__cvv">123</div>
  </section>

  <section class="card card-back" aria-label="Reverso de la tarjeta">
    <div class="card-back__stripe"></div>
    <div class="card-back__text">
      <p>la tarjeta BRENVICOR ha sido emirida y es propiradad de BRENVICOR S.L.U y a requerimento debe ser devuelta sin dilasion.</p>
      <p>El uso de esta tarjeta implica el conocimiento y aceptación del contrato entre las partes.</p>
      <p>En caso de pérdida o robo comuníquelo inmediatamente en el teléfono o dirección:</p>
    </div>
    <div class="card-back__web">www.brenvicor.es</div>
  </section>

</main>
</body>
</html>
```